Professional Sales Business looking for inspirational poster

I need an inspirational poster design for sales professionals, targeted around the phrase "Win Fast, Lose Fast". The style of the poster will be primarily minimalistic and flat with the main focus being on the phrase, however, any graphics or creative font and background styles are encouraged. Color choice is up to you.

Design Specs:
Vector files are best. If creating a vector file isn't possible, 150dpi raster images (at actual size or bigger) are good too. The poster must be in a portrait layout and scalable to the sizes of 18" X 24" and 24" X 36". Please convert all text to outlines.

Please msg me if you have any additional questions.

```html
<!DOCTYPE html>
<html lang="en">
<head>
<meta charset="utf-8">
<title>Win Fast, Lose Fast</title>
<link rel="stylesheet" href="https://fonts.googleapis.com/css2?family=Permanent+Marker&display=swap">
<style>
  :root {
    --frame: #1c1a1a;
    --wall-light: #b0494a;
    --wall-mid: #a3403f;
    --wall-dark: #923838;
    --chalk: #ffffff;
  }
  html, body {
    margin: 0;
    padding: 0;
    width: 910px;
    height: 1200px;
    overflow: hidden;
    background: var(--frame);
  }
  .poster {
    position: relative;
    width: 910px;
    height: 1200px;
    box-sizing: border-box;
    border: 9px solid var(--frame);
    border-bottom: 0;
    overflow: hidden;
  }
  .wall {
    position: absolute;
    inset: 0;
    background: linear-gradient(160deg, var(--wall-light) 0%, var(--wall-mid) 55%, var(--wall-dark) 100%);
  }
  .slogan {
    position: absolute;
    inset: 0;
    width: 100%;
    height: 100%;
  }
  .slogan-line {
    font-family: "Permanent Marker", cursive;
    font-size: 150px;
    fill: var(--chalk);
    letter-spacing: 4px;
  }
</style>
</head>
<body>
  <main class="poster">
    <div class="wall" role="img" aria-label="Red brick wall with pale mortar lines"></div>
    <svg class="slogan" viewBox="0 0 892 1200" aria-label="Win fast, lose fast">
      <defs>
        <path id="line-win" d="M 70 565 L 800 255"/>
        <path id="line-lose" d="M 62 720 Q 430 790 870 1010"/>
      </defs>
      <text class="slogan-line">
        <textPath href="#line-win">WIN FAST</textPath>
      </text>
      <text class="slogan-line">
        <textPath href="#line-lose">LOSE FAST</textPath>
      </text>
    </svg>
  </main>
</body>
</html>
```